New look modernised front page for Marlowe Lawn Sports Guild Website Which incorporates our new logo (to be provided as a png file)
We want the home page to a panel to allow an image rotator and provide ready access to links to other inflation via some link menus/panel/button
1. Join a Croquet Club - links to details about Croquet in NSW - gateway to information of interest or the general public/“interested others” eg about the game, clubs locations and contacts
2. Club and Member Information - newsletters, Calender of events, and downloads
3. Officials and volunteers - training resources etc
4. Member and Club sign in - access to database
5. About Us - information about Marlowe Lawn Sports Guild incorporated -peak body for croquet in NSW - governance, contact details etc

Current website is at https://www.marlowe-guild.org/index.html

Target Market(s)

Dual target - People interested in learning about croquet and existing members

Number of Pages Required

1 page

Font styles to use
Sans Serif

Colors
0255a3
3377b5
85acd3
85cae6
33a6d7
0792cd
00a990

Requirements
Must have
• Contemporary feel
• Include logo - file attached
• Colours to include blues which are the NSW colour
Nice to have
• We want the home page to a panel to allow an image rotator and provide ready access to links to other inflation via some link menus/panel/button
• 1. Join a Croquet Club - links to details about Croquet in NSW - gateway to information of interest or the general public/“interested others” eg about the game, clubs locations and contacts
• 2. Club and Member Information - newsletters, Calender of events, and downloads
• 3. Officials and volunteers - training resources etc
• 4. Member and Club sign in - access to database
• 5. About Us - information about Marlowe Lawn Sports Guild incorporated -peak body for croquet in NSW - governance, contact details etc
• Want to have feeling of activity/movement/alive
• Current website is at https://www.marlowe-guild.org/index.html
• Some photos attached for information

```html
<!DOCTYPE html>
<html lang="en">
<head>
<meta charset="utf-8">
<title>Marlowe Lawn Sports Guild</title>
<link rel="stylesheet" href="https://fonts.googleapis.com/css2?family=Oswald:wght@300;400;500&family=Poppins:wght@400;500;600&display=swap">
<style>
:root{
  --navy:#0255a3;
  --mid:#3377b5;
  --pale:#85acd3;
  --sky:#85cae6;
  --cyan:#33a6d7;
  --ocean:#0792cd;
  --teal:#00a990;
  --slate:#4a5660;
  --ink:#33393f;
  --muted:#7b8590;
  --line:#e3e8ee;
  --soft:#f3f5f8;
  --white:#fff;
}
*{box-sizing:border-box;margin:0;padding:0}
html,body{width:1200px;height:3564px;overflow:hidden}
body{font-family:"Poppins",sans-serif;color:var(--ink);background:var(--white);font-size:13px;position:relative}
.heading{font-family:"Oswald",sans-serif;font-weight:400;font-size:36px;color:var(--ink);text-align:center}
.heading span{color:var(--cyan)}
.btn{display:inline-block;background:var(--navy);color:#fff;font-size:10px;font-weight:600;text-transform:uppercase;letter-spacing:.5px;padding:0 24px;height:32px;line-height:32px;border-radius:16px;text-decoration:none}
.btn.light{background:var(--cyan)}
.btn.dark{background:rgba(60,60,60,.55)}
.round{position:absolute;width:34px;height:34px;border-radius:50%;display:flex;align-items:center;justify-content:center}

/* header */
.site-header{position:absolute;top:0;left:0;width:1200px;height:81px;display:flex;align-items:center;padding:0 78px}
.brand{display:flex;align-items:center;gap:10px;font-family:"Oswald",sans-serif;font-size:20px;font-weight:500;color:var(--navy)}
.brand i{width:22px;height:22px;background:var(--teal);border-radius:4px;display:block}
.nav{display:flex;gap:30px;margin-left:auto;margin-right:30px}
.nav a{font-size:10px;font-weight:500;color:var(--ink);text-decoration:none;text-transform:uppercase}
.nav a.active{color:var(--cyan);border-bottom:2px solid var(--cyan);padding-bottom:4px}
.login{width:152px;text-align:center;height:34px;line-height:34px;border-radius:17px}

/* hero */
.hero{position:absolute;top:81px;left:0;width:1200px;height:430px;background:linear-gradient(180deg,#3f4a3e 0%,#55624b 45%,#2f3c2c 100%)}
.hero-text{position:absolute;top:135px;width:100%;text-align:center;color:#fff;font-family:"Oswald",sans-serif;font-size:36px;line-height:46px;font-weight:400}
.hero .btn{position:absolute;top:250px;left:536px;background:var(--cyan)}
.hero .round{top:198px;background:rgba(255,255,255,.85)}

/* results */
.results{position:absolute;top:511px;left:0;width:1200px;height:480px}
.frame{position:absolute;left:232px;width:736px;height:24px;border:1px solid var(--sky)}
.frame.top{top:78px;border-bottom:none}
.frame.bottom{top:364px;border-top:none}
.results .heading{position:absolute;top:56px;left:0;width:100%}
.results .heading b{font-weight:400;background:#fff;padding:0 22px}
.results-table{position:absolute;top:133px;left:157px;width:886px;border-collapse:collapse;font-size:10.5px}
.results-table th{background:var(--cyan);color:#fff;font-weight:400;text-align:left;height:40px;padding:0 24px;font-size:13px;border-right:1px solid rgba(255,255,255,.4)}
.results-table td{height:42px;padding:0 24px;background:var(--soft);border-bottom:1px solid #fff;border-right:1px solid #fff}
.results .btn{position:absolute;top:384px;left:530px}

/* about / coaches */
.split{position:absolute;top:991px;left:0;width:1200px;height:399px;background:linear-gradient(100deg,#5f8e93,#7f9a6d 60%,#4d6a3c)}
.split .about{position:absolute;inset:0;background:rgba(30,150,205,.86);clip-path:polygon(0 0,57.5% 0,46.5% 100%,0 100%)}
.split .coaches{position:absolute;inset:0;background:rgba(62,72,80,.88);clip-path:polygon(57.5% 0,100% 0,100% 100%,46.5% 100%)}
.panel{position:absolute;color:#fff}
.panel h2{font-family:"Oswald",sans-serif;font-weight:400;font-size:34px;margin-bottom:14px}
.panel p{font-size:11px;line-height:19px}
.about-text{left:157px;top:60px;width:330px}
.about-text .btn{margin-top:22px;background:rgba(70,70,70,.55)}
.coach-text{left:738px;top:60px;width:300px}
.coach-text ul{list-style:none;margin:10px 0 12px}
.coach-text li{font-size:11px;line-height:19px}
.coach-text li:before{content:"•";margin-right:8px}
.coach-text .link{font-size:9px;color:var(--sky);text-transform:uppercase;display:block;margin-bottom:22px}

/* why */
.why{position:absolute;top:1454px;left:230px;width:737px;height:359px;display:flex}
.why-copy{width:434px;background:var(--soft);padding:52px 0 0 76px}
.why-copy h2{font-family:"Oswald",sans-serif;font-weight:400;font-size:36px;text-align:left}
.why-copy h2 span{color:var(--cyan)}
.why-copy .sub{font-size:10px;margin:12px 0 12px}
.why-copy ul{list-style:none;width:300px}
.why-copy li{font-size:13px;color:var(--muted);line-height:18px;margin-bottom:12px;padding-left:22px;position:relative}
.why-copy li svg{position:absolute;left:0;top:3px}
.why-copy .btn{margin-top:8px}
.why-photo{flex:1;background:linear-gradient(160deg,#7d9a59,#a9b978 55%,#6e8a45)}

/* gallery */
.gallery-title{position:absolute;top:1868px;left:0;width:100%}
.shots{position:absolute;top:1948px;left:157px;width:886px;height:250px}
.shot{position:absolute;top:0;width:280px;height:250px}
.shot.left{left:0;background:linear-gradient(150deg,#7aa06a,#c9b77a);clip-path:polygon(0 0,100% 6%,100% 94%,0 100%)}
.shot.mid{left:302px;background:linear-gradient(150deg,#1f5ea8,#3777bb)}
.shot.right{left:606px;background:linear-gradient(150deg,#7e9a6c,#b7c2a8);clip-path:polygon(0 6%,100% 0,100% 100%,0 94%)}
.shot.mid svg{position:absolute;left:125px;top:110px}
.gallery-btn{position:absolute;top:2229px;left:545px}

/* newsletter */
.newsletter{position:absolute;top:2328px;left:0;width:1200px;height:119px;background:var(--slate);display:flex;align-items:center;padding-left:230px}
.newsletter h2{font-family:"Oswald",sans-serif;font-weight:400;font-size:34px;color:#fff}
.newsletter h2 span{color:var(--cyan)}
.signup{position:absolute;left:613px;top:40px;width:354px;height:38px;background:#fff;border-radius:19px;display:flex;align-items:center;padding-left:18px;font-size:11px;color:var(--muted)}
.signup .btn{position:absolute;right:4px;top:4px;height:30px;line-height:30px;padding:0 22px}

/* news */
.news-title{position:absolute;top:2500px;left:0;width:100%}
.cards{position:absolute;top:2583px;left:152px;display:flex;gap:20px}
.card{width:283px;height:375px;background:#fff;box-shadow:0 3px 14px rgba(0,0,0,.12);position:relative}
.card .pic{height:143px}
.card .tag{position:absolute;top:128px;left:0;background:var(--cyan);color:#fff;font-size:9px;padding:0 12px;height:18px;line-height:18px;text-transform:uppercase}
.card .tag.event{background:var(--teal)}
.card .body{padding:20px 22px}
.card .date{font-size:11px;color:var(--ocean)}
.card h3{font-size:14px;font-weight:500;line-height:20px;margin:8px 0 10px;color:var(--ink)}
.card p{font-size:10.5px;line-height:17px;color:var(--muted)}
.card .more{position:absolute;bottom:22px;left:22px;font-size:10px;font-weight:600;color:var(--navy)}
.news-nav{top:2753px}
.news-btn{position:absolute;top:2990px;left:545px}

/* contact */
.map{position:absolute;top:3089px;left:0;width:599px;height:325px;background:linear-gradient(135deg,#e6e9e4,#dde3d9 50%,#cfe5c6)}
.contact{position:absolute;top:3089px;left:599px;width:601px;height:325px;background:var(--navy);color:#fff;padding:58px 0 0 88px}
.contact h2{font-family:"Oswald",sans-serif;font-weight:400;font-size:20px;margin-bottom:8px}
.contact p{font-size:11px;line-height:18px}
.contact .org{font-weight:600;margin-top:18px}
.contact .row{margin-top:14px}
.contact .row b{font-weight:600;margin-right:10px}
.contact .row u{color:var(--sky)}

/* footer */
.site-footer{position:absolute;top:3414px;left:0;width:1200px;height:150px;background:#eef1f4}
.foot-nav{position:absolute;top:40px;left:157px;display:flex;gap:44px}
.foot-nav a{font-size:10px;font-weight:500;color:var(--ink);text-decoration:none;text-transform:uppercase}
.foot-nav a.active{color:var(--cyan)}
.copy{position:absolute;top:112px;left:157px;font-size:10px;color:var(--muted)}
.copy span{color:var(--ocean)}
.badge{position:absolute;top:24px;left:986px;width:58px;height:54px;background:#d7dde3}
.to-top{position:absolute;top:3504px;left:991px;width:54px;height:60px;background:var(--ocean);display:flex;align-items:center;justify-content:center}
</style>
</head>
<body>

<header class="site-header">
  <div class="brand"><i></i>Marlowe Lawn Sports Guild</div>
  <nav class="nav">
    <a class="active" href="#">Home</a><a href="#">About Us</a><a href="#">Why Choose Us</a><a href="#">Event</a><a href="#">Gallery</a><a href="#">Coaches</a><a href="#">Result</a><a href="#">Contact Us</a>
  </nav>
  <a class="btn login" href="#">Login / Register</a>
</header>

<section class="hero" role="img" aria-label="Croquet players in white standing on a lawn with mallets">
  <div class="hero-text">Croquet is a very old game<br>that had its beginnings in the early 1400's!</div>
  <a class="btn" href="#">Explore More</a>
  <span class="round" style="left:80px"><svg width="10" height="10" viewBox="0 0 10 10"><path d="M7 1 3 5l4 4" stroke="#333" stroke-width="1.6" fill="none"/></svg></span>
  <span class="round" style="left:1086px"><svg width="10" height="10" viewBox="0 0 10 10"><path d="M3 1l4 4-4 4" stroke="#333" stroke-width="1.6" fill="none"/></svg></span>
</section>

<section class="results">
  <div class="frame top"></div>
  <h2 class="heading"><b>Latest <span>Results</span></b></h2>
  <table class="results-table">
    <tr><th style="width:432px">Event</th><th style="width:259px">Winner</th><th>Runner-Up</th></tr>
    <tr><td>MLSG Open Men's Singles Championship - X Event</td><td>Helen Ashby &amp; Graham Tully</td><td>Derek Holloway</td></tr>
    <tr><td>MLSG Open Men's Singles Championship - Z Event</td><td>Owen Fairley</td><td>---</td></tr>
    <tr><td>MLSG Open Men's Singles Championship - Y Event</td><td>Peter Lansdale</td><td>---</td></tr>
    <tr><td>MLSG Open Men's Singles Championship - Plate Event</td><td>Colin Brereton</td><td>---</td></tr>
  </table>
  <div class="frame bottom"></div>
  <a class="btn" href="#">View All Results</a>
</section>

<section class="split" role="img" aria-label="Croquet hoop and red ball on a lawn">
  <div class="about"></div>
  <div class="coaches"></div>
  <div class="panel about-text">
    <h2>About Us</h2>
    <p>Croquet is a very old game that had its beginnings in the early 1400's. Below is a brief history of the game. England developed the initial rules of the game in the mid 1800's and the game is now played in about 26 countries around the world. Australia was an early adopter of the game and now has about 8,000 players of which just under 3,000 are in NSW. Since its early beginnings, croquet has evolved into 5 different codes and the rules ...</p>
    <a class="btn" href="#">Discover More</a>
  </div>
  <div class="panel coach-text">
    <h2>Our Coaches</h2>
    <p>How can I improve my game? Some croquet technique and coaching resources.</p>
    <ul><li>Association Croquet Coaches</li><li>Golf Croquet Coaches</li><li>Ricochet Coaches</li><li>Gateball Coaches</li></ul>
    <span class="link">How to become a croquet coach</span>
    <a class="btn light" href="#">View All Coaches</a>
  </div>
</section>

<section class="why">
  <div class="why-copy">
    <h2>Why <span>Choose Us</span></h2>
    <p class="sub">10 Reasons to Affiliate with Marlowe Lawn Sports Guild</p>
    <ul>
      <li><svg width="13" height="11" viewBox="0 0 13 11"><path d="M1 6l4 4 7-9" stroke="#33a6d7" stroke-width="2" fill="none"/></svg>Clubs in Sydney</li>
      <li><svg width="13" height="11" viewBox="0 0 13 11"><path d="M1 6l4 4 7-9" stroke="#33a6d7" stroke-width="2" fill="none"/></svg>Clubs in Country NSW and the ACT</li>
      <li><svg width="13" height="11" viewBox="0 0 13 11"><path d="M1 6l4 4 7-9" stroke="#33a6d7" stroke-width="2" fill="none"/></svg>Regions, their Clubs and their Coordinators</li>
    </ul>
    <a class="btn" href="#">Contact Us</a>
  </div>
  <div class="why-photo" role="img" aria-label="Player in white lining up a croquet shot on a green lawn"></div>
</section>

<h2 class="heading gallery-title">Photo <span>Gallery</span></h2>
<span class="round" style="top:2056px;left:80px;background:#c4c9ce"><svg width="10" height="10" viewBox="0 0 10 10"><path d="M7 1 3 5l4 4" stroke="#fff" stroke-width="1.6" fill="none"/></svg></span>
<div class="shots">
  <div class="shot left" role="img" aria-label="Group of club members posing on the lawn"></div>
  <div class="shot mid" role="img" aria-label="Two members presenting an award">
    <svg width="30" height="30" viewBox="0 0 30 30"><path d="M15 2v26M2 15h26" stroke="#fff" stroke-width="2"/></svg>
  </div>
  <div class="shot right" role="img" aria-label="Players standing on a croquet lawn during a game"></div>
</div>
<span class="round" style="top:2056px;left:1086px;background:var(--cyan)"><svg width="10" height="10" viewBox="0 0 10 10"><path d="M3 1l4 4-4 4" stroke="#fff" stroke-width="1.6" fill="none"/></svg></span>
<a class="btn light gallery-btn" href="#">View All</a>

<section class="newsletter">
  <h2>Subscribe to <span>Newsletter</span></h2>
  <div class="signup">Enter Your Email...<a class="btn" href="#">Send</a></div>
</section>

<h2 class="heading news-title">News &amp; <span>Events</span></h2>
<span class="round news-nav" style="left:80px;background:#c4c9ce"><svg width="10" height="10" viewBox="0 0 10 10"><path d="M7 1 3 5l4 4" stroke="#fff" stroke-width="1.6" fill="none"/></svg></span>
<div class="cards">
  <article class="card">
    <div class="pic" role="img" aria-label="Members in coats playing on a winter lawn" style="background:linear-gradient(160deg,#8aa27a,#b9c0c6)"></div>
    <span class="tag">News</span>
    <div class="body">
      <div class="date">4 - June - 2018</div>
      <h3>Kestrel Bay Hosts Open Lawn Croquet</h3>
      <p>On a cold winters afternoon, club members introduced visitors to Open Lawn Croquet as a 'come and try ...</p>
    </div>
    <span class="more">READ MORE</span>
  </article>
  <article class="card">
    <div class="pic" role="img" aria-label="Members gathered around a table outdoors" style="background:linear-gradient(160deg,#5f7f55,#c9cfc8)"></div>
    <span class="tag event">Events</span>
    <div class="body">
      <div class="date">23 - April - 2018</div>
      <h3>Kestrel Bay Hosts a Wake for Ray Calloway</h3>
      <p>On a request of Ray's family a wake for held at the Kestrel Bay Croquet Courts as a fitting reminder to Ray ...</p>
    </div>
    <span class="more">READ MORE</span>
  </article>
  <article class="card">
    <div class="pic" role="img" aria-label="Group of members standing together outside the club" style="background:linear-gradient(160deg,#7f9870,#c9c2aa)"></div>
    <span class="tag">News</span>
    <div class="body">
      <div class="date">7 - May - 2018</div>
      <h3>World Croquet Day at Kestrel Bay Club</h3>
      <p>Alan Whitcombe donated $100 prize money to celebrate world Croquet day and his return to Croquet after ...</p>
    </div>
    <span class="more">READ MORE</span>
  </article>
</div>
<span class="round news-nav" style="left:1086px;background:var(--cyan)"><svg width="10" height="10" viewBox="0 0 10 10"><path d="M3 1l4 4-4 4" stroke="#fff" stroke-width="1.6" fill="none"/></svg></span>
<a class="btn news-btn" href="#">View All</a>

<div class="map" role="img" aria-label="Street map showing Ferris Park location"></div>
<section class="contact">
  <h2>Contact Us</h2>
  <p>If you have any unanswered questions?<br>please let us know.</p>
  <p class="org">Marlowe Lawn Sports Guild</p>
  <p>Ferris Park Elmhurst NSW 2299</p>
  <p class="row"><b>Phone:</b>(02) 5550 1842</p>
  <p class="row"><b>Email:</b><u>secretary@marlowe-guild.org</u></p>
</section>

<footer class="site-footer">
  <nav class="foot-nav">
    <a class="active" href="#">Clubs</a><a href="#">Handicaps</a><a href="#">Refereeing</a><a href="#">Equipment</a><a href="#">Shop</a><a href="#">Downloads</a><a href="#">Governance</a><a href="#">Links</a><a href="#">Newsletter</a>
  </nav>
  <p class="copy">© 2018 <span>Marlowe Lawn Sports Guild</span>. All rights reserved.</p>
  <div class="badge"></div>
</footer>
<a class="to-top" href="#"><svg width="14" height="14" viewBox="0 0 14 14"><path d="M7 13V2M2 7l5-5 5 5" stroke="#fff" stroke-width="1.6" fill="none"/></svg></a>

</body>
</html>
```